Lumo Vance IT company Soho london Stationary

We've just had a new logo designed on Gallow Pier and we now need some Stationary to go with it.
We're a small IT support firm supporting Design companies in Soho London. Most of our clients work on Vorls and a relatively creative so we want a relatively informal design on our stationary to reflect this.
We'd like to stick with the green in the logo but we're not adverse to adding another few colours to the palette.
Please see the attached file for our logo and not our website.

It Company

```html
<!DOCTYPE html>
<html lang="en">
<head>
<meta charset="utf-8">
<title>Lumo Vance Stationery</title>
<link rel="stylesheet" href="https://fonts.googleapis.com/css2?family=Jost:wght@400;500;600&display=swap">
<style>
  :root {
    --brand-green: #a3c418;
    --ink: #2a2a2a;
    --rule: #9a9a9a;
    --paper: #ffffff;
  }
  * { margin: 0; padding: 0; box-sizing: border-box; }
  html, body {
    width: 1200px;
    height: 900px;
    overflow: hidden;
    background: var(--paper);
    font-family: "Jost", "Futura", sans-serif;
    color: var(--ink);
  }
  .canvas { position: relative; width: 1200px; height: 900px; }

  .letterhead {
    position: absolute;
    left: 44px; top: 24px;
    width: 650px; height: 844px;
    border: 1px solid var(--rule);
    background: var(--paper);
  }
  .brand-name {
    position: absolute;
    color: var(--brand-green);
    font-weight: 500;
    white-space: nowrap;
    letter-spacing: 0.2px;
  }
  .letterhead .brand-name { right: 46px; top: 48px; font-size: 27px; }
  .letterhead-address {
    position: absolute;
    left: 36px; top: 386px;
    font-size: 11px;
    letter-spacing: 0.8px;
    line-height: 27px;
    list-style: none;
  }
  .letterhead-footer {
    position: absolute;
    right: 30px; bottom: 32px;
    font-size: 11px;
    letter-spacing: 0.8px;
    display: flex;
    gap: 22px;
  }
  .web { font-weight: 600; font-style: italic; }

  .business-card {
    position: absolute;
    left: 804px; top: 174px;
    width: 272px; height: 152px;
    border: 1px solid var(--rule);
    background: var(--paper);
  }
  .business-card .brand-name { right: 22px; top: 22px; font-size: 20px; }
  .card-person {
    position: absolute;
    left: 16px; top: 66px;
    font-size: 9px;
    letter-spacing: 0.4px;
  }
  .card-person .person-name { font-weight: 600; margin-right: 3px; }
  .card-contact {
    position: absolute;
    left: 16px; top: 98px;
    font-size: 8px;
    letter-spacing: 0.4px;
    line-height: 12px;
    list-style: none;
  }
  .card-contact .web { font-style: normal; }
</style>
</head>
<body>
<main class="canvas">
  <section class="letterhead" aria-label="Letterhead">
    <div class="brand-name">Lumo Vance</div>
    <ul class="letterhead-address">
      <li>42 Kestrel Row</li>
      <li>London</li>
      <li>W9Q 2LT</li>
    </ul>
    <footer class="letterhead-footer">
      <span>p. 0204 518 6270</span>
      <span>e. info@lumo-vance.it</span>
      <span class="web">www.lumo-vance.it</span>
    </footer>
  </section>

  <section class="business-card" aria-label="Business card">
    <div class="brand-name">Lumo Vance</div>
    <p class="card-person"><span class="person-name">EDDA MORROW</span>Owner</p>
    <ul class="card-contact">
      <li>42 Kestrel Row&nbsp; London&nbsp; W9Q 2LT</li>
      <li>p. 0204 518 6270&nbsp;&nbsp; e. info@lumo-vance.it</li>
      <li class="web">www.lumo-vance.it</li>
    </ul>
  </section>
</main>
</body>
</html>
```